A new company focused on starting and investing in transformative businesses.

We need a simple and clean website with a few pages. we like larkmeadow.com as a starting point. we want the landing page to be very simple with an option to click through on the top right into INVESTOR LOGIN. then we want to be able to scroll down to see more about our company.

Target Market(s)

professional

Coding

Coded - Design and coding required

Number of Pages Required

2 page

Font styles to use
Serif
Sans Serif

Requirements
Must have
• HALVERN BUILDERS logo (attached as a file) on the top with INVESTOR LOGIN as a click through on the right. Please model the click through from larkmeadow.com. The description (also written in attached file) should be on the landing page. we do not want to have to scroll to read the description.

Then we can scroll down to read more about Halvern including the mission and the two types of businesses. More is detailed on the attached file called "Halvern Website Syntax"
Should not have
• should not be slow loading with lots of fancy graphics. should not be busy and with too many colors.

```html
<!DOCTYPE html>
<html lang="en">
<head>
<meta charset="utf-8">
<title>Halvern Builders</title>
<link href="https://fonts.googleapis.com/css2?family=Lora:wght@400;500&display=swap" rel="stylesheet">
<style>
  :root {
    --navy: #021d33;
    --hero-blue: #0a84e6;
    --accent-blue: #0d5ea8;
    --paper: #f3f3f3;
    --page: #ffffff;
    --ink: #222222;
    --ink-soft: #555555;
    --ink-muted: #9a9a9a;
    --white: #ffffff;
  }
  * { margin: 0; padding: 0; box-sizing: border-box; }
  html, body {
    width: 1200px; height: 1200px; overflow: hidden;
    background: var(--page);
    font-family: "Lora", Georgia, serif;
  }
  .site {
    position: relative;
    width: 1200px; height: 1200px;
    overflow: hidden;
  }
  .hero {
    position: absolute; left: 128px; top: 0;
    width: 952px; height: 535px;
    background: var(--navy);
  }
  .brand {
    position: absolute;
    display: flex; align-items: center; gap: 10px;
    color: var(--white);
    font-weight: 500;
    letter-spacing: 0.06em;
    white-space: nowrap;
  }
  .brand-mark {
    display: block;
    background: var(--hero-blue);
  }
  .hero .brand { left: 98px; top: 24px; font-size: 17px; line-height: 22px; }
  .hero .brand-mark { width: 22px; height: 22px; }
  .hero-login {
    position: absolute; right: 106px; top: 24px;
    font-size: 17.5px; line-height: 22px;
    color: var(--hero-blue);
    text-decoration: none;
    white-space: nowrap;
  }
  .hero-bracket {
    position: absolute; left: 98px; top: 176px;
    width: 118px; height: 157px;
  }
  .hero-headline {
    position: absolute; left: 132px; top: 204px;
    width: 680px;
    color: var(--white);
    font-size: 36px; line-height: 44px; font-weight: 400;
  }
  .hero-headline .highlight { color: var(--hero-blue); }
  .scroll-arrow {
    position: absolute; left: 470px; top: 428px;
    width: 12px; height: 26px;
  }
  .about {
    position: absolute; left: 128px; top: 535px;
    width: 952px; height: 528px;
    background: var(--paper);
  }
  .mission {
    position: absolute; left: 139px; top: 109px;
    width: 700px;
    color: var(--ink);
    font-size: 25px; line-height: 38px;
  }
  .mission .highlight { color: var(--accent-blue); }
  .pillar { position: absolute; top: 230px; }
  .pillar-ground { left: 98px; width: 360px; }
  .pillar-special { left: 486px; width: 370px; top: 227px; }
  .pillar-title {
    color: var(--ink-soft);
    font-size: 17.5px; font-weight: 400;
    letter-spacing: 0.03em;
    margin-bottom: 11px;
  }
  .pillar-text {
    color: var(--ink-muted);
    font-size: 17.5px; line-height: 27.2px;
  }
  .footer {
    position: absolute; left: 128px; top: 1063px;
    width: 952px; height: 137px;
    background: var(--navy);
    color: var(--white);
  }
  .footer .brand { left: 98px; top: 36px; font-size: 14px; }
  .footer .brand-mark { width: 18px; height: 18px; }
  .footer-address {
    position: absolute; left: 98px; top: 87px;
    font-size: 12.5px; line-height: 14.5px;
    font-style: normal;
  }
  .copyright {
    position: absolute; left: 365px; top: 33px;
    font-size: 18px;
  }
  .media-contact {
    position: absolute; left: 365px; top: 87px;
    font-size: 12.5px; line-height: 14.5px;
  }
  .media-contact a { color: var(--hero-blue); text-decoration: none; }
  .investor-login {
    position: absolute; right: 106px; top: 33px;
    font-size: 17.5px;
    color: var(--hero-blue);
    text-decoration: none;
  }
</style>
</head>
<body>
<div class="site">
  <header class="hero">
    <div class="brand"><span class="brand-mark"></span>HALVERN BUILDERS</div>
    <a class="hero-login" href="#">Investor Login</a>
    <svg class="hero-bracket" viewBox="0 0 118 157" aria-hidden="true">
      <rect x="0" y="0" width="13" height="157" fill="#0a84e6"/>
      <rect x="0" y="0" width="118" height="12" rx="6" fill="#0a84e6"/>
      <rect x="0" y="0" width="20" height="12" fill="#0a84e6"/>
    </svg>
    <h1 class="hero-headline"><span class="highlight">Halvern Builders</span> is an entrepreneurial firm focused on building and growing transformational companies</h1>
    <svg class="scroll-arrow" viewBox="0 0 12 26" aria-hidden="true">
      <line x1="6" y1="1" x2="6" y2="24" stroke="#0a84e6" stroke-width="2"/>
      <polyline points="1,18 6,24 11,18" fill="none" stroke="#0a84e6" stroke-width="2"/>
    </svg>
  </header>

  <section class="about">
    <p class="mission">Our mission is to build <span class="highlight">meaningful</span> businesses that create <span class="highlight">enduring</span> value by impacting people in a <span class="highlight">measurable</span> way.</p>
    <article class="pillar pillar-ground">
      <h2 class="pillar-title">GROUND UP</h2>
      <p class="pillar-text">Our ground up business applies a proven analytic process to identify value edge, a form of competitive advantage. We architect transformational companies and are deliberate in creating the foundation necessary to lead an industry.</p>
    </article>
    <article class="pillar pillar-special">
      <h2 class="pillar-title">SPECIAL OPPORTUNITIES</h2>
      <p class="pillar-text">We partner with exceptional teams that create value by transforming lives. Our investment focus includes large companies and spin-outs.</p>
    </article>
  </section>

  <footer class="footer">
    <div class="brand"><span class="brand-mark"></span>HALVERN BUILDERS</div>
    <address class="footer-address">48 Alder Row<br>Westbrook, OR 97301</address>
    <p class="copyright">© 2021 Halvern Builders</p>
    <p class="media-contact">For media inquiries, please contact<br><a href="#">mara@halvernbuilders.com</a></p>
    <a class="investor-login" href="#">Investor Login</a>
  </footer>
</div>
</body>
</html>
```